Trendy, rustic, patriotic Facebook Design!

Would like something to catch people's eye! Must include our logo and phone number. 410-587-3920. Dogs in the project are a must. Bold pricing, location, etc to catch peoples eyes is a plus.

Target Market(s)

Dog owners

Font styles to use
Serif
Sans Serif

Colors
1f66ae
ec1f27
ffffff

Requirements
Must have
• Dogs, company logo, business phone 410-587-3920 and website www.furlowpaws.com
Nice to have
• Something that is rustic, trendy!
Should not have
• Cartoons.

```html
<!DOCTYPE html>
<html lang="en">
<head>
<meta charset="utf-8">
<title>Furlow Paws – Facebook Banners</title>
<link rel="stylesheet" href="https://fonts.googleapis.com/css2?family=Montserrat:wght@500;700&family=Tinos:wght@700&display=swap">
<style>
  :root{
    --navy:#002d6a;
    --red:#ec1f27;
    --white:#ffffff;
    --board:#d4d8df;
    --photo-a:#d9c3a3;
    --photo-b:#4a4440;
  }
  *{margin:0;padding:0;box-sizing:border-box}
  html,body{width:1067px;height:1200px;overflow:hidden;background:var(--board)}
  .board{position:relative;width:1067px;height:1200px}
  .banner{position:absolute;overflow:hidden;background:var(--navy);border:1px solid #1a1a1a}
  .banner .shapes{position:absolute;inset:0;width:100%;height:100%}
  .el{position:absolute;white-space:nowrap}
  .brand{position:absolute;display:flex;flex-direction:column;align-items:center;gap:6px;
    font-family:"Tinos",serif;font-weight:700;color:var(--navy);text-align:center;line-height:1}
  .brand .mark{width:34px;height:34px;border-radius:50%;background:var(--navy)}
  .headline{font-family:"Tinos",serif;font-weight:700;line-height:.95}
  .headline .white{color:var(--white)}
  .headline .red{color:var(--red)}
  .offer{position:absolute;border:2px solid var(--white);color:var(--white);
    font-family:"Montserrat",sans-serif;font-weight:700;display:flex;align-items:center;justify-content:center}
  .contact{position:absolute;display:flex;align-items:center;gap:8px;
    font-family:"Montserrat",sans-serif;font-weight:500;color:var(--white);line-height:1.35}
  .contact.on-white{color:var(--navy)}
  .contact svg{flex:none}
  .photo{position:absolute;border-radius:14px;
    background:radial-gradient(ellipse at 50% 45%,var(--photo-a) 0%,#b89770 40%,var(--photo-b) 75%,rgba(255,255,255,0) 100%)}
</style>
</head>
<body>
<svg width="0" height="0" style="position:absolute">
  <defs>
    <symbol id="icon-pin" viewBox="0 0 24 24"><path d="M12 2a7 7 0 0 0-7 7c0 5 7 13 7 13s7-8 7-13a7 7 0 0 0-7-7zm0 10a3 3 0 1 1 0-6 3 3 0 0 1 0 6z" fill="currentColor"/></symbol>
    <symbol id="icon-phone" viewBox="0 0 24 24"><path d="M6.6 3.5l3 3.2-1.8 2.6c1.3 2.7 3.6 5 6.3 6.3l2.6-1.8 3.2 3-1.7 3.2C11.6 20.3 3.7 12.4 3.4 5.2z" fill="currentColor"/></symbol>
    <symbol id="icon-globe" viewBox="0 0 24 24"><g fill="none" stroke="currentColor" stroke-width="1.4"><circle cx="12" cy="12" r="9.5"/><ellipse cx="12" cy="12" rx="4.2" ry="9.5"/><path d="M2.5 12h19M4 7h16M4 17h16"/></g></symbol>
  </defs>
</svg>

<main class="board">

  <!-- Wide cover banner -->
  <section class="banner" style="left:77px;top:42px;width:878px;height:232px">
    <svg class="shapes" viewBox="0 0 878 232">
      <circle cx="10" cy="-40" r="202" fill="var(--white)"/>
      <circle cx="782" cy="182" r="178" fill="var(--red)"/>
      <circle cx="772" cy="196" r="162" fill="var(--white)"/>
    </svg>
    <div class="brand" style="left:20px;top:48px;width:130px;font-size:19px"><span class="mark"></span>FURLOW PAWS</div>
    <div class="el headline" style="left:241px;top:26px">
      <div class="white" style="font-size:32px">WORLD-RENOWNED</div>
      <div class="red" style="font-size:43px">DOG TRAINING</div>
    </div>
    <div class="offer" style="left:303px;top:125px;width:226px;height:31px;font-size:17px">1 FREE CONSULTING</div>
    <div class="contact" style="left:25px;top:182px;font-size:12px"><svg width="13" height="15"><use href="#icon-pin"/></svg><span>1418 Harbor Mill Road<br>Millbrook MD 20419</span></div>
    <div class="contact" style="left:247px;top:195px;font-size:13px"><svg width="15" height="15"><use href="#icon-phone"/></svg>410-587-3920</div>
    <div class="contact" style="left:421px;top:193px;font-size:13px"><svg width="15" height="15"><use href="#icon-globe"/></svg>www.furlowpaws.com</div>
    <div class="photo" role="img" aria-label="Four dogs sitting together: a black-and-white collie, a golden retriever and two terriers" style="left:650px;top:45px;width:212px;height:180px"></div>
  </section>

  <!-- Large post banner -->
  <section class="banner" style="left:80px;top:321px;width:881px;height:443px">
    <svg class="shapes" viewBox="0 0 881 443">
      <circle cx="10" cy="-40" r="205" fill="var(--white)"/>
      <circle cx="822" cy="372" r="318" fill="var(--red)"/>
      <circle cx="810" cy="382" r="308" fill="var(--white)"/>
    </svg>
    <div class="brand" style="left:22px;top:52px;width:140px;font-size:20px"><span class="mark"></span>FURLOW PAWS</div>
    <div class="el headline" style="left:101px;top:167px">
      <div class="white" style="font-size:34px">WORLD-RENOWNED</div>
      <div class="red" style="font-size:46px">DOG TRAINING</div>
    </div>
    <div class="offer" style="left:166px;top:271px;width:237px;height:33px;font-size:19px">1 FREE CONSULTING</div>
    <div class="contact" style="left:35px;top:385px;font-size:12px"><svg width="13" height="15"><use href="#icon-pin"/></svg><span>1418 Harbor Mill Road<br>Millbrook MD 20419</span></div>
    <div class="contact" style="left:275px;top:391px;font-size:19px;gap:14px"><svg width="21" height="21"><use href="#icon-phone"/></svg>410-587-3920</div>
    <div class="contact on-white" style="left:565px;top:403px;font-size:13px"><svg width="15" height="15"><use href="#icon-globe"/></svg>www.furlowpaws.com</div>
    <div class="photo" role="img" aria-label="Four dogs sitting together: a black-and-white collie, a golden retriever and two terriers" style="left:560px;top:131px;width:305px;height:267px"></div>
  </section>

  <!-- Square post, left -->
  <section class="banner" style="left:80px;top:805px;width:423px;height:349px">
    <svg class="shapes" viewBox="0 0 423 349">
      <circle cx="0" cy="-40" r="150" fill="var(--white)"/>
      <circle cx="407" cy="293" r="207" fill="var(--red)"/>
      <circle cx="400" cy="302" r="200" fill="var(--white)"/>
    </svg>
    <div class="brand" style="left:12px;top:24px;width:110px;font-size:15px;gap:5px"><span class="mark" style="width:28px;height:28px"></span>FURLOW PAWS</div>
    <div class="el headline white" style="left:174px;top:20px;font-size:27px;line-height:1.18;color:var(--white)">WORLD<br>RENOWNED</div>
    <div class="el headline red" style="left:14px;top:138px;font-size:38px;line-height:1;color:var(--red)">DOG<br>TRAINING</div>
    <div class="offer" style="left:15px;top:234px;width:153px;height:22px;font-size:11.5px">1 FREE CONSULTING</div>
    <div class="contact" style="left:20px;top:321px;font-size:11px;gap:7px"><svg width="12" height="12"><use href="#icon-phone"/></svg>410-587-3920</div>
    <div class="contact on-white" style="left:243px;top:323px;font-size:12.5px"><svg width="14" height="14"><use href="#icon-globe"/></svg>www.furlowpaws.com</div>
    <div class="photo" role="img" aria-label="Four dogs sitting together: a black-and-white collie, a golden retriever and two terriers" style="left:234px;top:143px;width:185px;height:162px"></div>
  </section>

  <!-- Square post, right -->
  <section class="banner" style="left:537px;top:805px;width:423px;height:349px">
    <svg class="shapes" viewBox="0 0 423 349">
      <circle cx="0" cy="-40" r="150" fill="var(--white)"/>
      <circle cx="407" cy="293" r="207" fill="var(--red)"/>
      <circle cx="400" cy="302" r="200" fill="var(--white)"/>
    </svg>
    <div class="brand" style="left:12px;top:24px;width:110px;font-size:15px;gap:5px"><span class="mark" style="width:28px;height:28px"></span>FURLOW PAWS</div>
    <div class="el headline white" style="left:174px;top:20px;font-size:27px;line-height:1.18;color:var(--white)">WORLD<br>RENOWNED</div>
    <div class="el headline red" style="left:14px;top:138px;font-size:38px;line-height:1;color:var(--red)">DOG<br>TRAINING</div>
    <div class="offer" style="left:15px;top:234px;width:153px;height:22px;font-size:11.5px">1 FREE CONSULTING</div>
    <div class="contact" style="left:20px;top:321px;font-size:11px;gap:7px"><svg width="12" height="12"><use href="#icon-phone"/></svg>410-587-3920</div>
    <div class="contact on-white" style="left:243px;top:323px;font-size:12.5px"><svg width="14" height="14"><use href="#icon-globe"/></svg>www.furlowpaws.com</div>
    <div class="photo" role="img" aria-label="Four dogs sitting together: a black-and-white collie, a golden retriever and two terriers" style="left:234px;top:143px;width:185px;height:162px"></div>
  </section>

</main>
</body>
</html>
```